Graphics for New Online Software

Looking at a designer to design a UI/UX Interface for an Online Events Platform (just JPEG) and some corresponding images for a website content (i.e. features etc)

Deliverables:
1x User Interface Design for the Platform (refer to attachment)
5-6x Feature Listing Images (refer to attachment)

Target Market(s)

Technology, Online Users Etc

Industry/Entity Type

Software Developer

Number of Pages Required

1 page

Font styles to use
Sans Serif

Colors
34a7d8
0493ce
3176b5
85acd3

Requirements
Must have
• Looks like a well built software - examples:
https://brivatel.io/
https://quornity.com/

All the images should look very professional, as though you are using it on the online platform itself.
Nice to have
• Refer to attached "Feature Listing" and Logo

```html
<!DOCTYPE html>
<html lang="en">
<head>
<meta charset="utf-8">
<title>Eventra – Event Info</title>
<link rel="stylesheet" href="https://fonts.googleapis.com/css2?family=Rubik:wght@400;500;700;800&display=swap">
<style>
  :root {
    --navy: #1e2860;
    --ink: #14183a;
    --sky: #45c8fd;
    --royal: #2f5be8;
    --muted: #b5b8c2;
    --active-bg: #f1f4fd;
    --live-red: #e8141b;
    --amber-1: #f5b52e;
    --amber-2: #f9d243;
    --amber-3: #f8d67a;
    --white: #ffffff;
    --page: #f4f5f8;
  }
  * { box-sizing: border-box; margin: 0; padding: 0; }
  html, body { width: 1200px; height: 932px; overflow: hidden; }
  body {
    background: var(--page);
    font-family: "Rubik", Arial, sans-serif;
    color: var(--ink);
    position: relative;
  }
  .app {
    position: absolute; left: 46px; top: 83px;
    width: 1108px; height: 749px;
    background: var(--white);
    overflow: hidden;
  }
  .sidebar {
    position: absolute; left: 0; top: 0; width: 222px; height: 100%;
    border-right: 1px solid #9fd9f5; border-left: 1px solid #9fd9f5; border-bottom: 1px solid #9fd9f5;
  }
  .brand {
    position: absolute; left: 36px; top: 50px;
    display: flex; align-items: center; gap: 6px;
    font-weight: 700; font-size: 18px; color: var(--ink); letter-spacing: -0.3px;
  }
  .brand-dot { width: 14px; height: 14px; background: var(--royal); }
  .nav { list-style: none; position: absolute; top: 139px; left: 0; width: 100%; }
  .nav-item {
    height: 44px; display: flex; align-items: center; gap: 17px;
    padding-left: 38px; font-size: 11.5px; font-weight: 500; color: var(--muted);
    margin-bottom: 7.5px; position: relative;
  }
  .nav-item svg { width: 21px; height: 18px; fill: #c5c7cd; }
  .nav-item.is-active { background: var(--active-bg); color: var(--ink); }
  .nav-item.is-active svg { fill: var(--sky); }
  .nav-item.is-active::after {
    content: ""; position: absolute; right: 0; top: 5px; width: 4px; height: 32px;
    background: var(--royal); border-radius: 2px 0 0 2px;
  }
  .hero {
    position: absolute; left: 222px; top: 0; width: 886px; height: 291px;
    background:
      radial-gradient(circle at 82% 55%, var(--amber-3) 0 22%, transparent 23%),
      linear-gradient(110deg, var(--amber-1) 0%, var(--amber-2) 45%, #f8d970 100%);
  }
  .hero-title {
    position: absolute; left: 71px; top: 155px;
    color: var(--white); font-weight: 800; font-size: 30px; line-height: 39px;
  }
  .details { position: absolute; left: 293px; top: 338px; width: 747px; height: 85px; }
  .when {
    position: absolute; left: 0; top: 0; height: 85px; padding-left: 27px;
    border-left: 6px solid var(--sky);
  }
  .when-date { font-size: 20px; font-weight: 700; margin-top: 18px; }
  .when-time { font-size: 14px; margin-top: 6px; }
  .about {
    position: absolute; left: 248px; top: 6px; width: 482px;
    font-size: 10.5px; line-height: 21.7px; color: var(--ink);
  }
  .live-banner {
    position: absolute; left: 293px; top: 469px; width: 747px; height: 88px;
    background: var(--navy); border-radius: 6px; overflow: hidden; color: var(--white);
  }
  .live-ring {
    position: absolute; left: 30px; top: -8px; width: 104px; height: 104px;
    border-radius: 50%; background: #3e4777;
  }
  .live-core {
    position: absolute; left: 20px; top: 20px; width: 64px; height: 64px;
    border-radius: 50%; background: #636c98; display: flex; align-items: center; justify-content: center;
  }
  .live-status { position: absolute; left: 180px; top: 34px; font-size: 14.5px; font-weight: 700; }
  .live-tag { background: var(--live-red); padding: 1px 3px; }
  .time-left { position: absolute; left: 372px; top: 38px; width: 150px; font-size: 10.5px; }
  .time-left strong { position: absolute; right: 0; top: 0; font-weight: 700; }
  .time-bar { position: absolute; left: 0; top: 17px; width: 150px; height: 2px; background: var(--live-red); }
  .time-bar span { display: block; width: 50px; height: 100%; background: var(--white); }
  .join {
    position: absolute; left: 608px; top: 27px; width: 97px; height: 33px;
    background: var(--sky); border-radius: 3px; color: var(--white);
    font-size: 10.5px; font-weight: 700; display: flex; align-items: center; justify-content: center;
  }
  .section-title {
    position: absolute; left: 222px; width: 886px; top: 614px; text-align: center;
    font-size: 20px; font-weight: 500; color: var(--ink);
  }
  .section-title::after {
    content: ""; display: block; width: 65px; height: 3px; background: var(--sky);
    border-radius: 2px; margin: 7px auto 0;
  }
  .speaker-card {
    position: absolute; top: 689px; width: 163px; height: 80px;
    background: var(--sky); border-radius: 6px 6px 0 0;
  }
</style>
</head>
<body>
<main class="app">
  <aside class="sidebar">
    <div class="brand"><span>EVENTRA</span><span class="brand-dot"></span></div>
    <ul class="nav">
      <li class="nav-item is-active">
        <svg viewBox="0 0 20 18"><path d="M10 1 1 9h3v8h4v-5h4v5h4V9h3z"/></svg>Event Info</li>
      <li class="nav-item">
        <svg viewBox="0 0 20 18"><rect x="1" y="4" width="12" height="10" rx="1"/><path d="M14 8l5-3v8l-5-3z"/></svg>Stage</li>
      <li class="nav-item">
        <svg viewBox="0 0 20 18"><circle cx="6" cy="5" r="3"/><circle cx="14" cy="5" r="3"/><path d="M0 16c0-4 3-6 6-6s6 2 6 6zM9 16c0-4 2-6 5-6s6 2 6 6z"/></svg>Breakouts</li>
      <li class="nav-item">
        <svg viewBox="0 0 20 18"><path d="M2 1h16l2 5H0zM2 7h16v10h-6v-5H8v5H2zM4 10h3v3H4z"/></svg>Booths</li>
      <li class="nav-item">
        <svg viewBox="0 0 20 18"><path d="M1 2h18v14H1zm2 12h14l-4-6-3 4-2-2zM6 5a2 2 0 1 0 0 .1z"/></svg>Virtual Exhibition</li>
      <li class="nav-item">
        <svg viewBox="0 0 20 18"><path d="M2 6h16v4H2zM3 11h6v6H3zm8 0h6v6h-6zM10 6C7 1 4 3 6 6m4 0c3-5 6-3 4 0"/></svg>Rewards</li>
    </ul>
  </aside>

  <section class="hero" role="img" aria-label="Conference banner artwork: warm yellow line pattern with a large round badge">
    <h1 class="hero-title">Scriptora Conference<br>Singapore 2020</h1>
  </section>

  <section class="details">
    <div class="when">
      <p class="when-date">23 Jun 2020</p>
      <p class="when-time">1:00 PM - 9:30 PM UTC</p>
    </div>
    <p class="about">Lorem ipsum dolor sit amet, consectetur adipiscing elit. Integer vel elit id arcu feugiat egestas. Nam vitae est magna. Aenean quis tristique nulla, eu vulputate dolor. Donec in dolor non velit mollis tristique. Fusce tempor non dui sit amet eleifend.</p>
  </section>

  <section class="live-banner">
    <div class="live-ring">
      <div class="live-core">
        <svg width="34" height="22" viewBox="0 0 34 22"><rect x="0" y="0" width="23" height="22" rx="2" fill="#fff"/><path d="M25 11l8-7v14z" fill="#fff"/></svg>
      </div>
    </div>
    <p class="live-status">Stage is <span class="live-tag">Live</span> Now</p>
    <div class="time-left">Time Left <strong>8h 53m</strong>
      <div class="time-bar"><span></span></div>
    </div>
    <div class="join">Join Stage</div>
  </section>

  <h2 class="section-title">Speakers</h2>
  <div class="speaker-card" style="left:352px"></div>
  <div class="speaker-card" style="left:585px"></div>
  <div class="speaker-card" style="left:818px"></div>
</main>
</body>
</html>
```